2-Sided Law Firm Business Card

This is the second phase of a law firm "rebrand project" in which I'm changing my firm's name to "Brackwood Law PLLC." The first phase was a logo contest -- I will be updating this project sometime tomorrow with the winning logo design.

The business card will need to include, on its reverse side, the firm's logo and tag line, "Practical Counsel for Growing Ventures," on a darker background whose color is consistent with the logo design.

The face of the card will need to include the firm's name (logo), website url, and phone number. It will also need to include, at the very least, the name of the attorney, the attorney's title, the attorney's email address, and the attorney's twitter feed. (I do not maintain a dedicated office and therefore the card does not need to specify a business address.) I will provide the actual contact information to the winning designer. Until then, you may use fictional data in suggesting your proposed design.

My firm specializes in representing startup companies. This means I routinely interact with young entrepreneurs and the (typically) older, more experienced investors who fund them. I need to appeal to the former without offending the latter. I'm interesting in conveying the idea that my firm is a credible alternative to larger, brand-name firms. I use these words in positioning my firm in this market: creative; flexible; fair; practical; experienced. The winning design needs to convey this idea.

I'm will also be re-working my website soon and will likely use noto sans and noto serif as my primary website fonts. I'd like the business card to use a font that is similar, but also compatible with the font used in the firm's logo.

Target Market(s)

Young entrepreneurs and older investors who collaborate in the formation and funding of high-tech startup companies located in the Pacific Northwest.

Industry/Entity Type

Law Firm

Font styles to use
Serif
Sans Serif

Requirements
Must have
• Firm logo, firm tag line, firm website url, firm phone number, attorney name, attorney title, attorney email address, and attorney twitter.

The attached pdf indicates kind of what I have in mind, recognizing that it is my amateur attempt at doing what I'm hoping the winning designer is able to do so much better.
Nice to have
• Adding a statement about my practice areas, if there's room, might be nice:

"General Counsel | Business Formation | Intellectual Property | Angel Investments & Venture Capital | Mergers & Acquisitions"

Also, I make it a point to meet with clients "by appointment only" in the following areas of Seattle: "Northgate | Harbor Point | Eastfield | Lakeview Commons." It might be worth including as well, but only if the card itself isn't too cramped. I favor "too simple" over "too informative."
Should not have
• Do NOT put the scales of justice anywhere on this business card. I am a business lawyer.

```html
<!DOCTYPE html>
<html lang="en">
<head>
<meta charset="utf-8">
<title>Brackwood Law PLLC – Business Card</title>
<link rel="stylesheet" href="https://fonts.googleapis.com/css2?family=Lato:wght@300;400;700&display=swap">
<style>
  :root{
    --bg:#e9e6e1;
    --ink:#0b0b0b;
    --paper:#f4f4f4;
    --paper-shade:#d9d9d9;
    --text-light:#f2f2f2;
    --text-muted:#bdbdbd;
    --firm-grey:#8a8a8a;
    --rule:#6c6c6c;
    --strip-text:#333;
  }
  *{box-sizing:border-box;margin:0;padding:0}
  html,body{width:1200px;height:1023px;overflow:hidden}
  body{background:var(--bg);font-family:"Lato",Arial,sans-serif;position:relative}

  .card{position:absolute;width:620px;height:354px;border-radius:22px;overflow:hidden;
        box-shadow:0 10px 28px rgba(0,0,0,.25)}

  /* front */
  .card--front{left:60px;top:110px;
        background:linear-gradient(160deg,#2a2a2a 0%,var(--ink) 45%,var(--ink) 100%)}
  .front__firm{position:absolute;left:36px;top:34px;color:var(--firm-grey);
        font-weight:400;font-size:34px;line-height:1;white-space:nowrap}
  .front__areas{position:absolute;left:36px;top:98px;color:var(--text-muted);
        font-size:15.5px;line-height:1.35;font-weight:400}
  .front__rule{position:absolute;left:36px;right:34px;top:150px;height:1px;background:var(--rule)}
  .front__person{position:absolute;left:36px;top:172px;color:var(--text-light)}
  .front__name{font-weight:700;font-size:18px}
  .front__title{font-size:14px;color:var(--text-muted);margin-top:2px}
  .front__short-rule{width:160px;height:1px;background:var(--rule);margin:12px 0 10px}
  .contact{display:flex;align-items:center;gap:8px;font-size:14px;color:var(--text-muted);margin-top:5px;white-space:nowrap}
  .contact svg{width:13px;height:13px;flex:none}
  .front__online{position:absolute;right:40px;top:232px}
  .front__strip{position:absolute;left:0;right:0;bottom:0;height:44px;
        background:linear-gradient(180deg,var(--paper),var(--paper-shade));
        display:flex;align-items:center;padding-left:36px;
        color:var(--strip-text);font-size:14px;letter-spacing:.2px}

  /* back */
  .card--back{left:520px;top:560px;
        background:linear-gradient(180deg,var(--paper),var(--paper-shade))}
  .back__band{position:absolute;left:0;right:0;top:88px;height:178px;
        background:linear-gradient(160deg,#262626 0%,var(--ink) 40%,var(--ink) 100%);
        display:flex;flex-direction:column;justify-content:center;padding-left:60px}
  .back__firm{color:var(--text-light);font-weight:400;font-size:44px;line-height:1;white-space:nowrap}
  .back__tagline{color:var(--text-light);font-weight:700;font-size:15px;margin-top:14px}
</style>
</head>
<body>

<section class="card card--front" aria-label="Card front">
  <p class="front__firm">Brackwood Law PLLC</p>
  <p class="front__areas">General Counsel | Business Formation | Intellectual Property<br>Angel Investments &amp; Venture Capital | Mergers &amp; Acquisitions</p>
  <div class="front__rule"></div>

  <div class="front__person">
    <p class="front__name">Dean R. Hollis</p>
    <p class="front__title">Startup Attorney</p>
    <div class="front__short-rule"></div>
    <p class="contact">
      <svg viewBox="0 0 14 14"><rect x="1" y="1" width="12" height="12" rx="2" fill="none" stroke="currentColor"/><path d="M4.5 3.5c0 4 2 6 6 6l.5-1.5-2-1-1 1c-1-.5-2-1.5-2.5-2.5l1-1-1-2z" fill="currentColor"/></svg>
      425.555.0148
    </p>
    <p class="contact">
      <svg viewBox="0 0 14 14"><rect x="1.5" y="2.5" width="11" height="9" rx="1" fill="none" stroke="currentColor"/><line x1="1.5" y1="5" x2="12.5" y2="5" stroke="currentColor"/></svg>
      brackwoodlawpllc.com
    </p>
  </div>

  <div class="front__online">
    <p class="contact">
      <svg viewBox="0 0 14 14"><rect x="1" y="2.5" width="12" height="9" rx="1" fill="currentColor"/><path d="M1.5 3.5l5.5 4 5.5-4" fill="none" stroke="#000"/></svg>
      dean@brackwoodlawpllc.com
    </p>
    <p class="contact">
      <svg viewBox="0 0 14 14"><rect x="1" y="1" width="12" height="12" rx="2" fill="currentColor"/></svg>
      @deanhollis
    </p>
  </div>

  <div class="front__strip">Northgate | Harbor Point | Eastfield | Lakeview Commons</div>
</section>

<section class="card card--back" aria-label="Card back">
  <div class="back__band">
    <p class="back__firm">Brackwood Law PLLC</p>
    <p class="back__tagline">Practical Counsel for Growing Ventures</p>
  </div>
</section>

</body>
</html>
```